Fiber Optic Internet flyer promotion Winter 2016-2017

I am looking for a marketing flyer that will not be folded, single sided that will advertise a Fiber Optic internet promotion that we are currently running.

The design should be clean, flow well, quickly grab attention, and if a very few short seconds list what the promotion is, and direct them to contact us.

It needs to list a few features of the promotion, but does not need to be in this order and should flow well with the flyer
1.) Fiber Optic Internet
2.) 100 Mbits for $140 /month or 150 Mbits for $190 /month
3.) Free construction cost up to $10,000, limited funds available.
4.) Limited time offer. Must commit before funds run out.

(555) 274-3916, www.kelvoranet.example

Target Market(s)

Small to large business

Industry/Entity Type

Internet Service Provider

Requirements
Must have
• Eye catching appeal. Quickly convey the message of the promotion and our company name and phone number.
Should not have
• Our company is primarily a wireless ISP. This promotion is all about Fiber Optic. I do not want to draw attention to the "wireless" portion of our business with this flyer.

```html
<!DOCTYPE html>
<html lang="en">
<head>
<meta charset="utf-8">
<title>Kelvora Networks – Fiber Optic Internet Flyer</title>
<link href="https://fonts.googleapis.com/css2?family=Roboto+Condensed:ital,wght@0,400;0,700;1,400&display=swap" rel="stylesheet">
<style>
  :root {
    --page-bg: #e9ecef;
    --paper: #ffffff;
    --pale-cyan: #cfe8ee;
    --pale-cyan-light: #e4f3f6;
    --blue-deep: #1c4fb0;
    --blue-mid: #2f7fd6;
    --blue-light: #6fc3ea;
    --red: #e21b22;
    --red-dark: #7a0c10;
    --grey-band: #c9cdd3;
    --ink: #3a3a3a;
    --navy: #1f2f7a;
  }
  html, body {
    margin: 0;
    width: 1200px;
    height: 1000px;
    overflow: hidden;
    background: var(--page-bg);
    font-family: "Roboto Condensed", "Arial Narrow", sans-serif;
  }
  .flyer {
    position: absolute;
    left: 360px;
    top: 30px;
    width: 480px;
    height: 940px;
    background: var(--paper);
    box-shadow: 0 4px 18px rgba(0,0,0,0.18);
    overflow: hidden;
  }
  .flyer-art { position: absolute; inset: 0; }
  .headline text { font-weight: 700; fill: #ffffff; }
  .band-title { font-weight: 400; fill: #ffffff; }
  .intro {
    position: absolute;
    left: 58px;
    top: 490px;
    width: 330px;
    margin: 0;
    font-style: italic;
    font-size: 13.5px;
    line-height: 18px;
    color: var(--ink);
    transform: rotate(-4deg);
    transform-origin: left top;
  }
  .offer {
    position: absolute;
    margin: 0;
    font-size: 15px;
    line-height: 18px;
    color: var(--ink);
  }
  .offer-title { text-transform: uppercase; display: block; }
  .offer--choices { right: 62px; top: 612px; text-align: right; }
  .offer--choices ul { list-style: none; margin: 2px 0 0; padding: 0; text-align: left; }
  .offer--choices li::before { content: "\25B8\00a0"; font-size: 12px; }
  .offer--construction { left: 70px; top: 700px; }
  .offer--deadline { right: 62px; top: 782px; text-align: right; }
  .brand {
    position: absolute;
    left: 0;
    right: 0;
    top: 824px;
    display: flex;
    justify-content: center;
    align-items: center;
    gap: 10px;
  }
  .brand-dot { width: 22px; height: 22px; border-radius: 50%; background: var(--red); }
  .brand-name { font-size: 26px; font-weight: 700; color: var(--navy); letter-spacing: 0.5px; }
  .contact-lead {
    position: absolute;
    left: 0; right: 0;
    top: 872px;
    text-align: center;
    font-style: italic;
    font-size: 13px;
    color: #5a5a5a;
  }
  .contact {
    position: absolute;
    left: 0; right: 0;
    top: 898px;
    display: flex;
    justify-content: center;
    gap: 26px;
    font-size: 15px;
    font-weight: 700;
    color: #333;
  }
  .contact-item { display: flex; align-items: center; gap: 6px; }
</style>
</head>
<body>
  <main class="flyer">
    <svg class="flyer-art" width="480" height="940" viewBox="0 0 480 940">
      <defs>
        <linearGradient id="headline-blue" x1="0" y1="0" x2="0" y2="1">
          <stop offset="0" stop-color="#1f5cc4"/>
          <stop offset="0.55" stop-color="#2f8ad8"/>
          <stop offset="1" stop-color="#6fbfe9"/>
        </linearGradient>
        <linearGradient id="fiber-tone" x1="0" y1="0" x2="1" y2="1">
          <stop offset="0" stop-color="#b0141a"/>
          <stop offset="0.6" stop-color="#6e0a0e"/>
          <stop offset="1" stop-color="#3a0507"/>
        </linearGradient>
      </defs>

      <rect class="bg-top" width="480" height="380" fill="var(--pale-cyan)"/>
      <polygon class="bg-top-stripe" points="0,0 220,0 0,70" fill="var(--pale-cyan-light)"/>
      <polygon class="bg-bottom" points="0,770 0,940 430,940" fill="var(--pale-cyan)"/>
      <polygon class="bg-bottom-light" points="300,940 480,860 480,940" fill="var(--pale-cyan-light)"/>

      <polygon class="headline-panel" points="0,105 480,20 480,345 0,365" fill="url(#headline-blue)"/>
      <g class="headline" transform="rotate(-4 240 200)">
        <text x="20" y="166" font-size="60" textLength="425" lengthAdjust="spacingAndGlyphs">CONNECTIVITY</text>
        <text x="20" y="250" font-size="98" textLength="430" lengthAdjust="spacingAndGlyphs">YOU CAN</text>
        <text x="20" y="333" font-size="88" textLength="425" lengthAdjust="spacingAndGlyphs">DEPEND ON</text>
      </g>

      <polygon class="separator" points="0,365 480,345 480,362 0,382" fill="var(--grey-band)"/>

      <polygon class="offer-band" points="0,382 480,362 480,560 0,455" fill="var(--red)"/>
      <polygon class="fiber-photo" role="img" aria-label="Close-up photo of glowing red fiber optic strands"
               points="235,505 480,395 480,560" fill="url(#fiber-tone)"/>
      <g transform="rotate(-3 240 420)">
        <text class="band-title" x="70" y="430" font-size="34" textLength="330" lengthAdjust="spacingAndGlyphs">A FIBER OPTIC INTERNET</text>
        <text class="band-title" x="50" y="454" font-size="19" textLength="250" lengthAdjust="spacingAndGlyphs">FOR YOUR BUSINESS MATTERS</text>
      </g>

      <polygon class="tab tab--choices" points="420,612 480,600 480,672 420,662" fill="var(--blue-mid)"/>
      <polygon class="tab tab--construction" points="0,690 62,678 58,738 0,745" fill="var(--red)"/>
      <polygon class="tab tab--deadline" points="425,782 480,772 480,818 425,812" fill="var(--blue-light)"/>
    </svg>

    <p class="intro">Waiting on<br>a slow expensive<br>internet connection can add<br>hours of frustration and reduced<br>productivity. KELVORA NETWORKS offer a<br>latest technology to maximize internet data transfer on<br>reliable speed using fiber optic.</p>

    <div class="offer offer--choices">
      <span class="offer-title">Choices:</span>
      <ul>
        <li>100 Mbits for $140 /month</li>
        <li>150 Mbits for $190 /month</li>
      </ul>
    </div>

    <p class="offer offer--construction"><span class="offer-title">Free Construction</span>cost up to $10,000,<br>limited funds available</p>

    <p class="offer offer--deadline"><span class="offer-title">Limited Time Offer</span>Must commit before funds run out</p>

    <div class="brand">
      <span class="brand-dot"></span>
      <span class="brand-name">KELVORA NETWORKS</span>
    </div>

    <div class="contact-lead">Contact Us For Further Info:</div>
    <div class="contact">
      <span class="contact-item">
        <svg width="16" height="20" viewBox="0 0 16 20" aria-hidden="true"><rect x="3" y="1" width="10" height="18" rx="2" fill="none" stroke="#333" stroke-width="1.6"/><line x1="6" y1="16" x2="10" y2="16" stroke="#333" stroke-width="1.6"/></svg>
        (555) 274-3916
      </span>
      <span class="contact-item">
        <svg width="20" height="20" viewBox="0 0 20 20" aria-hidden="true"><circle cx="10" cy="10" r="8.5" fill="none" stroke="#333" stroke-width="1.6"/><ellipse cx="10" cy="10" rx="3.8" ry="8.5" fill="none" stroke="#333" stroke-width="1.3"/><line x1="1.5" y1="10" x2="18.5" y2="10" stroke="#333" stroke-width="1.3"/></svg>
        www.kelvoranet.example
      </span>
    </div>
  </main>
</body>
</html>
```